Drowsy Heron

Need a business card for our restaurant. Restaurant and Bar in the mountains of North Idaho. Rustic looking card

Contact Information for Business Card

rustic design, wood and metal looking, primarily neutral colors

Requirements
Must have
• Name, address, phone number, website, email address

```html
<!DOCTYPE html>
<html lang="en">
<head>
<meta charset="utf-8">
<title>The Drowsy Heron – Business Card</title>
<link rel="stylesheet" href="https://fonts.googleapis.com/css2?family=Nunito+Sans:wght@400;600;800&display=swap">
<style>
  :root {
    --backdrop: #d2d5d6;
    --wood-light: #c0905f;
    --wood-mid: #b07e4f;
    --wood-dark: #9e6c40;
    --ink: #111111;
    --paper: #ffffff;
  }
  * { box-sizing: border-box; margin: 0; padding: 0; }
  html, body { width: 900px; height: 1200px; overflow: hidden; }
  body {
    background: var(--backdrop);
    font-family: "Nunito Sans", Arial, sans-serif;
    color: var(--ink);
    position: relative;
  }
  .card {
    position: absolute;
    left: 136px;
    width: 630px;
    height: 357px;
    border-radius: 11px;
    overflow: hidden;
  }
  .card--front { top: 216px; }
  .card--back { top: 629px; background: var(--paper); }

  .wood-surface {
    position: absolute; inset: 0;
    background: linear-gradient(175deg, var(--wood-mid) 0%, var(--wood-light) 45%, var(--wood-mid) 70%, var(--wood-dark) 100%);
  }
  .brand-seal {
    position: absolute;
    display: flex; align-items: center; justify-content: center;
    text-align: center;
  }
  .brand-seal svg { position: absolute; inset: 0; }
  .brand-seal__name {
    position: relative;
    font-weight: 800;
    text-transform: uppercase;
    line-height: 1.2;
    letter-spacing: 0.08em;
    color: var(--ink);
  }
  .card--front .brand-seal { left: 181px; top: 45px; width: 268px; height: 268px; }
  .card--front .brand-seal__name { font-size: 24px; }
  .card--back .brand-seal { left: 63px; top: 72px; width: 214px; height: 214px; }
  .card--back .brand-seal__name { font-size: 19px; }

  .contact {
    position: absolute;
    left: 300px; top: 70px;
  }
  .contact__name { font-size: 23px; font-weight: 800; letter-spacing: 0.02em; line-height: 1.1; }
  .contact__role { font-size: 14px; font-weight: 600; margin-top: 2px; }
  .contact__address { font-size: 14px; font-weight: 600; line-height: 23px; margin-top: 32px; letter-spacing: 0.03em; }
  .contact__list { list-style: none; margin-top: 18px; }
  .contact__item {
    display: flex; align-items: center; gap: 7px;
    font-size: 14px; font-weight: 600; letter-spacing: 0.03em;
    height: 29px;
  }
  .contact__item--phone { letter-spacing: 0.2em; }
  .contact__item svg { width: 15px; height: 15px; flex: none; }
</style>
</head>
<body>

<section class="card card--front">
  <div class="wood-surface" role="img" aria-label="Warm brown wood grain texture"></div>
  <div class="brand-seal">
    <svg viewBox="0 0 268 268" aria-hidden="true">
      <circle cx="134" cy="134" r="130" fill="none" stroke="var(--ink)" stroke-width="6"/>
    </svg>
    <p class="brand-seal__name">The<br>Drowsy Heron</p>
  </div>
</section>

<section class="card card--back">
  <div class="brand-seal">
    <svg viewBox="0 0 214 214" aria-hidden="true">
      <circle cx="107" cy="107" r="103" fill="none" stroke="var(--ink)" stroke-width="5"/>
    </svg>
    <p class="brand-seal__name">The<br>Drowsy Heron</p>
  </div>

  <div class="contact">
    <h1 class="contact__name">MARTIN COLE</h1>
    <p class="contact__role">Founder</p>
    <p class="contact__address">214 Cedar Ave,<br>Pinehollow, ID 83999</p>
    <ul class="contact__list">
      <li class="contact__item contact__item--phone">
        <svg viewBox="0 0 24 24" aria-hidden="true"><path fill="var(--ink)" d="M6.6 10.8a15 15 0 0 0 6.6 6.6l2.2-2.2a1 1 0 0 1 1-.25 11.4 11.4 0 0 0 3.6.6 1 1 0 0 1 1 1V20a1 1 0 0 1-1 1A17 17 0 0 1 3 4a1 1 0 0 1 1-1h3.5a1 1 0 0 1 1 1c0 1.25.2 2.45.6 3.6a1 1 0 0 1-.25 1z"/></svg>
        (208) 555-0147
      </li>
      <li class="contact__item">
        <svg viewBox="0 0 24 24" aria-hidden="true"><path fill="var(--ink)" d="M2 5h20v14H2z"/><path fill="none" stroke="var(--paper)" stroke-width="2" d="M3 6l9 7 9-7"/></svg>
        info@thedrowsyheronpinehollow.com
      </li>
      <li class="contact__item">
        <svg viewBox="0 0 24 24" aria-hidden="true"><g fill="none" stroke="var(--ink)" stroke-width="2"><circle cx="12" cy="12" r="9"/><ellipse cx="12" cy="12" rx="4" ry="9"/><path d="M3 12h18M5 7h14M5 17h14"/></g></svg>
        thedrowsyheronpinehollow.com
      </li>
    </ul>
  </div>
</section>

</body>
</html>
```